B2B EDM Banner Design- Specialist Tech Company

We need a new top-of-email banner for our EDM campaigns for Varnel Brix (www.varnelbrix-example.com
). This banner will sit at the top of every email and must immediately signal the brand, look modern and professional, and be visually aligned with the tech/IT audience.
Size of the banner: Around 728x90 - it must fit at the top of an email blast.
Purpose of the Banner
Establish a strong, recognizable brand identity across all Varnel Brix EDMs
visually consistent with existing banners created for other brands (see reference examples provided)
Communicate Varnel Brix’s value proposition at a glance
Brand Name
Varnel Brix
Tagline (must appear in the banner)
“11,322 whitepapers from 726 companies”
Design Requirements
Style & Tone
Modern, clean, and professional
Tech-centric look and feel
High-quality, sleek, and corporate
Eye-catching but not cluttered
Should feel premium and authoritative
Layout & Composition
Full-width banner for email header
Horizontal orientation similar to the Plomtar and Quindle Staff Archive examples
Include space for the brand name/logo prominently on the left or centered
Integrate the tagline in a readable, secondary position
Optional: a subtle background texture or tech-related abstract pattern (circuitry, network nodes, gradient, etc.)
No busy imagery—should feel clean and trustworthy
Color Palette
Use colors consistent with Varnel Brix branding from www.varnelbrix-example.com
Blues, greys, blacks, and tech-style gradients preferred
Should feel consistent with a B2B IT audience
Typography
Clean, sans-serif fonts (professional/tech-aligned)
Brand name should be bold and prominent
Tagline should be smaller, but still readable on desktop and mobile
Imagery (if used)
Abstract tech shapes, network visuals, geometric patterns, or gradient overlays
Avoid photography of people
Keep imagery subtle so text remains legible
Call-to-Action Button (optional)
None required in this banner (unlike the HR examples)
Banner should remain a pure brand header
Deliverables
Final banner in PNG and JPG formats
2–3 design variations (if possible) for A/B testing
Dimensions optimized for EDM: ~600–700px wide (standard email width), proportionate height

```html
<!DOCTYPE html>
<html lang="en">
<head>
<meta charset="utf-8">
<title>Varnel Brix – EDM Header Banners</title>
<link rel="stylesheet" href="https://fonts.googleapis.com/css2?family=Poppins:wght@400;500;700&display=swap">
<style>
  :root {
    --stage: #808080;
    --navy: #00305a;
    --navy-deep: #002a50;
    --sky: #009fe0;
    --white: #ffffff;
  }
  html, body {
    margin: 0;
    padding: 0;
    width: 1200px;
    height: 838px;
    overflow: hidden;
    background: var(--stage);
    font-family: "Poppins", sans-serif;
  }
  .banner {
    position: absolute;
    left: 76px;
    width: 1047px;
    height: 130px;
    overflow: hidden;
  }
  .banner--light { top: 230px; background: var(--white); }
  .banner--dark  { top: 478px; background: var(--navy); }
  .banner__art {
    position: absolute;
    inset: 0;
    width: 1047px;
    height: 130px;
  }
  .brand {
    position: absolute;
    left: 40px;
    top: 0;
    height: 130px;
    display: flex;
    align-items: center;
    gap: 12px;
  }
  .brand__dot {
    width: 40px;
    height: 40px;
    border-radius: 50%;
    background: var(--sky);
    flex: none;
  }
  .brand__text { display: inline-flex; flex-direction: column; }
  .brand__name {
    font-weight: 700;
    font-size: 26px;
    line-height: 28px;
    letter-spacing: -0.3px;
    white-space: nowrap;
    padding-bottom: 2px;
    border-bottom: 1.5px solid var(--sky);
  }
  .brand__tagline {
    display: block;
    font-weight: 500;
    font-size: 7.5px;
    line-height: 10px;
    letter-spacing: 2px;
    margin-top: 3px;
    text-align: justify;
    text-align-last: justify;
    white-space: nowrap;
  }
  .headline {
    position: absolute;
    left: 318px;
    top: 0;
    height: 130px;
    margin: 0;
    display: flex;
    flex-direction: column;
    justify-content: center;
    font-weight: 500;
    font-size: 28px;
    line-height: 33px;
    letter-spacing: -0.2px;
    white-space: nowrap;
  }
  .headline__num { font-weight: 700; }
  .headline__small { font-size: 15px; font-weight: 400; }

  .banner--light .brand__name,
  .banner--light .brand__tagline,
  .banner--light .headline__num,
  .banner--light .headline__small { color: var(--navy); }
  .banner--light .headline__word { color: var(--sky); }

  .banner--dark .brand__name,
  .banner--dark .brand__tagline,
  .banner--dark .headline__num,
  .banner--dark .headline__small { color: var(--white); }
  .banner--dark .headline__word { color: var(--sky); }
</style>
</head>
<body>

<section class="banner banner--light">
  <svg class="banner__art" viewBox="0 0 1047 130" xmlns="http://www.w3.org/2000/svg">
    <defs>
      <linearGradient id="waveLight" x1="0" x2="1" y1="0" y2="0">
        <stop offset="0" stop-color="#b7e2f7" stop-opacity="0.1"/>
        <stop offset="0.6" stop-color="#8fd2f3" stop-opacity="0.35"/>
        <stop offset="1" stop-color="#b7e2f7" stop-opacity="0.1"/>
      </linearGradient>
    </defs>
    <path role="img" aria-label="Fine flowing line wave pattern in pale blue"
          fill="url(#waveLight)"
          d="M0,95 C120,125 220,120 340,100 C460,80 560,85 680,110 C740,122 790,124 850,118 L850,130 C780,134 720,132 660,124 C560,108 460,104 340,118 C220,132 110,130 0,112 Z"/>
    <path fill="var(--navy)"
          d="M690,0 C740,10 770,45 810,80 C850,112 900,125 960,122 C1000,120 1030,110 1047,100 L1047,0 Z"/>
    <path fill="var(--sky)"
          d="M720,0 C765,12 795,50 830,78 C870,105 920,114 970,112 C1005,110 1030,102 1047,90 L1047,0 Z"/>
    <ellipse role="img" aria-label="Circuit board pattern radiating from a central hub"
             cx="965" cy="32" rx="112" ry="72" fill="var(--navy)"/>
  </svg>

  <div class="brand">
    <div class="brand__dot"></div>
    <div class="brand__text">
      <span class="brand__name">VARNEL BRIX</span>
      <span class="brand__tagline">FOR IT PROFESSIONALS</span>
    </div>
  </div>

  <h1 class="headline">
    <span><span class="headline__num">11322</span> <span class="headline__word">Whitepapers</span> <span class="headline__small">from</span></span>
    <span><span class="headline__num">726</span> <span class="headline__word">Companies</span></span>
  </h1>
</section>

<section class="banner banner--dark">
  <svg class="banner__art" viewBox="0 0 1047 130" xmlns="http://www.w3.org/2000/svg">
    <defs>
      <linearGradient id="waveDark" x1="0" x2="1" y1="0" y2="0">
        <stop offset="0" stop-color="#1a8fd8" stop-opacity="0.2"/>
        <stop offset="0.6" stop-color="#20a4ec" stop-opacity="0.5"/>
        <stop offset="1" stop-color="#1a8fd8" stop-opacity="0.2"/>
      </linearGradient>
      <linearGradient id="bandDark" x1="0" x2="1" y1="0" y2="1">
        <stop offset="0" stop-color="#0a86cf"/>
        <stop offset="0.6" stop-color="#0170b5"/>
        <stop offset="1" stop-color="#34b4f0"/>
      </linearGradient>
    </defs>
    <path role="img" aria-label="Fine flowing line wave pattern in bright blue"
          fill="url(#waveDark)"
          d="M0,95 C120,125 220,120 340,100 C460,80 560,85 680,110 C740,122 790,124 850,118 L850,130 C780,134 720,132 660,124 C560,108 460,104 340,118 C220,132 110,130 0,112 Z"/>
    <path fill="var(--white)"
          d="M690,0 C740,10 770,45 810,80 C850,112 900,125 960,122 C1000,120 1030,110 1047,100 L1047,0 Z"/>
    <path fill="url(#bandDark)"
          d="M720,0 C765,12 795,50 830,78 C870,105 920,114 970,112 C1005,110 1030,102 1047,90 L1047,0 Z"/>
    <ellipse cx="965" cy="32" rx="114" ry="74" fill="none" stroke="var(--white)" stroke-width="1.5"/>
    <ellipse role="img" aria-label="Circuit board pattern radiating from a central hub"
             cx="965" cy="32" rx="111" ry="71" fill="var(--navy-deep)"/>
  </svg>

  <div class="brand">
    <div class="brand__dot"></div>
    <div class="brand__text">
      <span class="brand__name">VARNEL BRIX</span>
      <span class="brand__tagline">FOR IT PROFESSIONALS</span>
    </div>
  </div>

  <h1 class="headline">
    <span><span class="headline__num">11322</span> <span class="headline__word">Whitepapers</span> <span class="headline__small">from</span></span>
    <span><span class="headline__num">726</span> <span class="headline__word">Companies</span></span>
  </h1>
</section>

</body>
</html>
```